シンプルな名刺が希望です。ロゴの配列及び色は変えてもよいです。
https://www.pelmora.jp/file/message/4733158
表面  会社名 名前 〒 住所 tel  fax アドレス 携帯電話
表面で窮屈であれば裏面も使ってもよいです。
こちらの方が提案者様が使いやすいとの事で、ロゴ作成者様より提案がありました。
https://www.pelmora.jp/file/message/4735157
https://www.pelmora.jp/file/message/4735158
宜しくお願いします。
EPSファイルでロゴを作成したものを添付します。

これなら読めないでしょうか。

シンプルで気に入りました。

ありがとうございました。

```html
<!DOCTYPE html>
<html lang="ja">
<head>
<meta charset="UTF-8">
<title>アルテナ 名刺</title>
<link rel="stylesheet" href="https://fonts.googleapis.com/css2?family=Noto+Sans+JP:wght@300;400&display=swap">
<style>
  :root {
    --card-bg: #ffffff;
    --band-blue: #1ea2e6;
    --text-light: #ffffff;
  }
  html, body {
    margin: 0;
    padding: 0;
    width: 726px;
    height: 1200px;
    overflow: hidden;
    background: var(--card-bg);
  }
  .business-card {
    display: block;
    width: 726px;
    height: 1200px;
  }
  .band { fill: var(--band-blue); }
  .company-name,
  .person-name,
  .contact-line {
    fill: var(--text-light);
    font-family: "Noto Sans JP", sans-serif;
  }
  .company-name { font-size: 52px; font-weight: 300; letter-spacing: 4px; }
  .person-name { font-size: 46px; font-weight: 300; letter-spacing: 2px; }
  .contact-line { font-size: 29px; font-weight: 300; }
</style>
</head>
<body>
<svg class="business-card" viewBox="0 0 726 1200" xmlns="http://www.w3.org/2000/svg">
  <polygon class="band band-top" points="0,77 726,312 726,420 0,182"/>
  <text class="company-name" x="340" y="232" text-anchor="middle" transform="rotate(17 340 214)">アルテナ</text>

  <polygon class="band band-middle" points="0,533 726,542 726,648 0,630"/>
  <text class="person-name" x="350" y="618" text-anchor="middle">森川　拓</text>

  <polygon class="band band-bottom" points="0,924 726,792 726,1200 0,1200"/>
  <g class="contact-block" transform="rotate(-8 190 1000)">
    <text class="contact-line" x="190" y="1000">〒　東京都目黒区〇〇〇</text>
    <text class="contact-line" x="190" y="1038">tel　  000-5678</text>
    <text class="contact-line" x="190" y="1076">fax アドレス　 111-369</text>
    <text class="contact-line" x="190" y="1114">携帯電話　073-555-0142</text>
  </g>
</svg>
</body>
</html>
```